Forking Well Buisiness card

needing a Business card for our company - Forking Well.
Forking well is co owned by Jess and Owen Marchetti (Husband and Wife)
Services Forking Well provides include:
Dietetic/nutrition Consultations, weight loss coaching programs, personal and group training, post injury rehab, health and nutrition presentations and Health Retreats.
Jess:
Accredited Practicing Dietitian & Personal trainer
Owen:
Personal trainer, rehab trainer & Strength and conditioning coach
At this stage the business cards will be made just for Jess.
She has a training studio in Armadale and Dietetics private practice in Richmond.
Mobile services are also available (i.e. meet at house or local cafe)

We need the card to look smart, modern and combine both nutrition and training.
We already have a logo which I will attach.
I was initial thinking i black background but am open to suggestions.

Target Market(s)

Health concious, People with money,

Industry/Entity Type

Nutrition

Contact Information for Business Card

Forking Well
Jess Marchetti
M: 0417390265
E: forkingwell@mailnest.com
W: www.forkingwell.com.au
Address:
Dietetics: Level 1, 583 Bellow Street
Richmond VIC 3121
Training: Private Studio, behind 2087 Tamsin St
ARMADALE, VIC, 3143

Requirements
Must have
• Must have logo (see attached) please not the one we use is the top left (blue and green)
please note attachment is top left (green and blue)

needs to be clear to read - the font needs to be clear and sharp and the background cannot be too busy.eg funny patterns.
Could I please see a card with a line for 'appointment time/date:' possibly on the back. Would like to see what this looks like.
Jess Marchetti's Profile (side of card) must include "Accredited Practicing Dietitian" and "Personal Trainer."
I like when the services forking well provide are in dot form.
Nice to have
• would like the card to be 2 sides
first side:
Forking well logo - Large
services forking well provides: Dietetic/nutrition Consultations, weight loss coaching programs, personal and group training, post injury rehab, health and nutrition presentations and Health Retreats.
web address
second side:
smaller logo
Details for Jess:
Accredited Practicing Dietitian
Personal Trainer
Contact Details:
M: 0417390265
E: forkingwell@mailnest.com
Address:
Richmond VIC 3121
ARMADALE, VIC, 3143
Should not have
• Dietetic + nutrition consultations
Should say dietetic/nutrition consultations (first letter of words in capitals please)
Please write phone number as 0417 390 265
Not: 04 17 390265
- note numbers as 4, 3, 3.

```html
<!DOCTYPE html>
<html lang="en">
<head>
<meta charset="utf-8">
<title>Forking Well Business Card</title>
<link href="https://fonts.googleapis.com/css2?family=Nunito+Sans:wght@300;400;600;700;800&display=swap" rel="stylesheet">
<style>
  :root {
    --brand-blue: #0f54a3;
    --brand-green: #7dbb2d;
    --ink: #333333;
    --faint-blue: #6f97cf;
    --paper: #ffffff;
    --backdrop: #e4e4e4;
  }
  * { margin: 0; padding: 0; box-sizing: border-box; }
  html, body { width: 1056px; height: 1200px; overflow: hidden; }
  body {
    background: var(--backdrop);
    font-family: "Nunito Sans", Arial, sans-serif;
    position: relative;
  }
  .card {
    position: absolute;
    left: 87px;
    width: 882px;
    background: var(--paper);
    overflow: hidden;
    box-shadow: 0 1px 4px rgba(0,0,0,0.18);
  }
  .card--front { top: 93px; height: 488px; }
  .card--back { top: 634px; height: 490px; }
  .card__waves { position: absolute; inset: 0; width: 100%; height: 100%; }

  .brand {
    position: absolute;
    display: flex;
    align-items: center;
    gap: 16px;
  }
  .brand__dot { border-radius: 50%; flex: none; }
  .brand__name { font-weight: 600; white-space: nowrap; letter-spacing: -0.5px; }

  .card--front .brand { left: 34px; top: 176px; }
  .card--front .brand__dot { width: 46px; height: 46px; background: var(--brand-green); }
  .card--front .brand__name { font-size: 50px; color: var(--brand-blue); }

  .services {
    position: absolute;
    left: 451px; top: 73px;
    list-style: none;
    color: var(--brand-blue);
    font-size: 20px;
    font-weight: 400;
    line-height: 30px;
    text-transform: uppercase;
  }
  .services li { position: relative; padding-left: 27px; margin-bottom: 4px; }
  .services li::before {
    content: "";
    position: absolute;
    left: 2px; top: 11px;
    width: 10px; height: 10px;
    border-top: 3px solid var(--brand-green);
    border-right: 3px solid var(--brand-green);
    border-radius: 0 10px 0 0;
    transform: rotate(-20deg);
  }

  .website {
    position: absolute;
    left: 0; right: 0; top: 420px;
    text-align: center;
    color: var(--paper);
    font-size: 27px;
    font-weight: 700;
    letter-spacing: 0.5px;
  }

  .card--back .brand { left: 62px; top: 52px; }
  .card--back .brand__dot { width: 44px; height: 44px; background: var(--faint-blue); }
  .card--back .brand__name { font-size: 46px; color: var(--faint-blue); font-weight: 400; }

  .profile { position: absolute; left: 62px; top: 242px; color: var(--brand-blue); }
  .profile__name { font-size: 30px; font-weight: 800; line-height: 36px; }
  .profile__role { font-size: 20px; font-weight: 400; line-height: 26px; }
  .profile__roles { margin-top: 6px; }

  .contact { position: absolute; left: 62px; top: 350px; list-style: none; color: var(--brand-blue); }
  .contact li { display: flex; align-items: center; gap: 10px; font-size: 23px; font-weight: 700; height: 36px; }
  .contact svg { flex: none; }

  .locations { position: absolute; left: 493px; top: 242px; color: var(--ink); font-size: 20px; line-height: 26px; }
  .location + .location { margin-top: 26px; }
  .location__label { color: var(--brand-green); font-weight: 700; }
  .location:nth-child(2) .location__label { color: var(--brand-blue); }
</style>
</head>
<body>

<section class="card card--front">
  <svg class="card__waves" viewBox="0 0 710 393" preserveAspectRatio="none" aria-hidden="true">
    <path d="M0,282 C80,305 170,325 240,330 C150,336 60,322 0,306 Z" fill="var(--brand-green)"/>
    <path d="M0,322 C120,345 240,340 360,320 C480,300 600,284 710,300 V393 H0 Z" fill="var(--brand-blue)"/>
    <path d="M500,292 C590,284 660,294 710,310 V338 C660,314 590,296 500,292 Z" fill="var(--brand-green)" stroke="var(--paper)" stroke-width="2"/>
  </svg>

  <div class="brand">
    <span class="brand__dot"></span>
    <span class="brand__name">Forking Well</span>
  </div>

  <ul class="services">
    <li>Dietetic/Nutrition Consultations</li>
    <li>Weight Loss Coaching Programs</li>
    <li>Personal and Group Training</li>
    <li>Post Injury Rehab</li>
    <li>Health &amp; Nutrition Presentations<br>and Health Retreats</li>
  </ul>

  <p class="website">www.forkingwell.com.au</p>
</section>

<section class="card card--back">
  <svg class="card__waves" viewBox="0 0 710 395" preserveAspectRatio="none" aria-hidden="true">
    <path d="M0,0 H710 V70 C560,72 420,100 300,124 C200,140 90,122 0,84 Z" fill="var(--brand-blue)"/>
    <path d="M0,90 C90,126 200,144 300,130 C200,152 80,142 0,114 Z" fill="var(--brand-green)"/>
    <path d="M0,114 C80,142 200,152 300,130 C200,160 80,150 0,122 Z" fill="var(--brand-blue)"/>
    <path d="M470,94 C560,80 640,76 710,80 V110 C650,94 560,88 470,94 Z" fill="var(--brand-green)"/>
  </svg>

  <div class="brand">
    <span class="brand__dot"></span>
    <span class="brand__name">Forking Well</span>
  </div>

  <div class="profile">
    <h1 class="profile__name">Jess Marchetti</h1>
    <div class="profile__roles">
      <p class="profile__role">Accredited Practicing Dietitian</p>
      <p class="profile__role">Personal Trainer</p>
    </div>
  </div>

  <ul class="contact">
    <li>
      <svg width="22" height="28" viewBox="0 0 22 28" aria-hidden="true">
        <rect x="3" y="1.5" width="16" height="25" rx="3" fill="none" stroke="var(--brand-blue)" stroke-width="2.2"/>
        <line x1="3" y1="21" x2="19" y2="21" stroke="var(--brand-blue)" stroke-width="1.8"/>
        <circle cx="11" cy="24" r="1.2" fill="var(--brand-blue)"/>
      </svg>
      <span>0417 390 265</span>
    </li>
    <li>
      <svg width="26" height="18" viewBox="0 0 26 18" aria-hidden="true">
        <rect x="1" y="1" width="24" height="16" fill="none" stroke="var(--brand-blue)" stroke-width="1.8"/>
        <path d="M1,1 L13,10 L25,1" fill="none" stroke="var(--brand-blue)" stroke-width="1.8"/>
      </svg>
      <span>forkingwell@mailnest.com</span>
    </li>
  </ul>

  <div class="locations">
    <div class="location">
      <p class="location__label">Dietetics:</p>
      <p>Level 1, 583 Bellow Street</p>
      <p>Richmond VIC 3121</p>
    </div>
    <div class="location">
      <p class="location__label">Training:</p>
      <p>Private Studio, behind 2087 Tamsin St</p>
      <p>ARMADALE, VIC, 3143</p>
    </div>
  </div>
</section>

</body>
</html>
```